Lip Balm tube design

create label/ product print design for Lip balm tubes
Size of tube
76 mm high
24 mm wide

2.75 x 2" h- this is for the main part of tube, not top cap

Current design has been attached for reference. Would like to stick to something similar but need it to "pop" more and be more readable to user
Designs
Vanilla Mint
Citrus Spice
Coconut Lime
Marshmallow Creme
Satsuma Sugar

Designs must include product information (ingredients) as detailed on examples.
Color palette is color but soft, matte tones

```html
<!DOCTYPE html>
<html lang="en">
<head>
<meta charset="utf-8">
<title>Lip Balm Tube Labels</title>
<link rel="stylesheet" href="https://fonts.googleapis.com/css2?family=Cormorant+Garamond:wght@400;500&family=Allura&display=swap">
<style>
  :root {
    --stage: #676a70;
    --vanilla-bg: #dcdedd; --vanilla-tab: #6c829e;
    --marsh-bg: #f8f0e6; --marsh-tab: #c4a18a;
    --coco-bg: #cfdfa9; --coco-tab: #9bae63;
    --citrus-bg: #d2875c; --citrus-tab: #b45f31;
    --on-tab: #ffffff;
  }
  * { box-sizing: border-box; margin: 0; padding: 0; }
  html, body { width: 1200px; height: 1081px; overflow: hidden; background: var(--stage); }
  .canvas { position: relative; width: 1200px; height: 1081px; }

  .label { position: absolute; overflow: hidden; background: var(--bg); color: var(--ink); }
  .label--front { width: 134px; height: 424px; }
  .label--wrap { width: 283px; height: 389px; }

  .vanilla { --bg: var(--vanilla-bg); --tab: var(--vanilla-tab); --ink: var(--vanilla-tab); --art: #b6c2d2; }
  .marsh   { --bg: var(--marsh-bg); --tab: var(--marsh-tab); --ink: var(--marsh-tab); --art: #e6d1c1; }
  .coco    { --bg: var(--coco-bg); --tab: var(--coco-tab); --ink: #8fa35a; --art: #b9cd8c; }
  .citrus  { --bg: var(--citrus-bg); --tab: var(--citrus-tab); --ink: #b45f31; --art: #c4764b; }

  .tab {
    position: absolute; top: 0; background: var(--tab); color: var(--on-tab);
    border-radius: 0 0 42px 42px;
  }
  .label--front .tab { left: 27px; width: 80px; height: 290px; }
  .label--wrap .tab { left: 29px; width: 75px; height: 270px; border-radius: 0 0 38px 38px; }

  .tab__kind {
    position: absolute; left: 8px; right: 8px; top: 34px;
    font-family: "Cormorant Garamond", serif; font-size: 12.5px; letter-spacing: .3px;
    text-align: center; padding: 2px 0 1px;
    border-top: 1px solid var(--on-tab); border-bottom: 1px solid var(--on-tab);
  }
  .label--wrap .tab__kind { top: 30px; font-size: 11.5px; }

  /* title is laid out horizontally, then turned to read bottom-to-top */
  .title {
    position: absolute; left: 50%; top: 170px;
    width: 216px; height: 80px;
    transform: translate(-50%, -50%) rotate(-90deg);
  }
  .label--wrap .title { top: 159px; width: 206px; height: 75px; }
  .title__name {
    position: absolute; left: 20px; top: 6px;
    display: inline-block; white-space: nowrap;
    font-family: "Cormorant Garamond", serif; font-weight: 500; line-height: 1;
    font-size: var(--name-size, 42px); letter-spacing: -.5px;
  }
  .title__flavour {
    position: absolute; right: -4px; top: calc(100% - 12px);
    font-family: "Allura", cursive; font-size: 28px; line-height: 1; font-weight: 400;
    letter-spacing: 0; white-space: nowrap;
  }
  .title__flavour::before {
    content: ""; position: absolute; right: 100%; top: 62%;
    width: 70px; height: 1px; margin-right: 3px; background: currentColor;
  }

  .art { position: absolute; background: linear-gradient(160deg, var(--art), var(--bg)); opacity: .85; }
  .label--front .art--base { left: 0; right: 0; bottom: 0; height: 140px; border-radius: 50% 50% 0 0 / 30% 30% 0 0; }
  .label--wrap .art--base { left: 0; bottom: 0; width: 170px; height: 130px; border-radius: 0 60% 0 0; }
  .label--wrap .art--corner { right: 0; top: 0; width: 125px; height: 140px; border-radius: 0 0 0 70%;
    background: linear-gradient(220deg, var(--art), var(--bg)); }

  .info {
    position: absolute; left: 176px; top: 84px; width: 98px; height: 290px;
    writing-mode: vertical-rl; transform: rotate(180deg);
    display: flex; flex-direction: column; gap: 4px;
    font-family: "Cormorant Garamond", serif; color: var(--ink);
  }
  .info__claims {
    display: flex; justify-content: space-between; padding: 0 4px;
    font-family: "Allura", cursive; font-size: 20px; line-height: 1;
  }
  .info__ingredients { font-size: 5.6px; line-height: 1.45; padding-left: 4px; }
  .info__ingredients strong { font-weight: 400; display: block; }
  .info__maker { font-size: 4.8px; line-height: 1.6; padding-left: 6px; letter-spacing: .2px; }
</style>
</head>
<body>
<main class="canvas">

  <!-- Vanilla Mint -->
  <section class="label label--front vanilla" style="left:102px;top:94px">
    <div class="art art--base" role="img" aria-label="Line drawing of vanilla orchid flowers and pods"></div>
    <div class="tab">
      <div class="tab__kind">LIP BALM</div>
      <div class="title"><span class="title__name" style="--name-size:44px">VANILLA<span class="title__flavour">mint</span></span></div>
    </div>
  </section>
  <section class="label label--wrap vanilla" style="left:273px;top:130px">
    <div class="art art--corner" role="img" aria-label="Line drawing of vanilla orchid flowers"></div>
    <div class="art art--base" role="img" aria-label="Line drawing of vanilla orchid flowers and pods"></div>
    <div class="tab">
      <div class="tab__kind">LIP BALM</div>
      <div class="title"><span class="title__name" style="--name-size:42px">VANILLA<span class="title__flavour">mint</span></span></div>
    </div>
    <div class="info">
      <div class="info__claims"><span>plant based</span><span>vegan</span><span>cruelty free</span></div>
      <p class="info__ingredients"><strong>Ingredients:</strong>Organic Olive Fruit Oil (Olea Europaea), Organic Coconut Oil (Cocos Nucifera), Organic Shea Butter (Butyrospermum Parkii), Organic Jojoba Seed Oil (Simmondsia Chinensis), Rosehip Seed Oil (Rosa Canina), Vitamin E (Tocopherol), Sunflower Seed Oil (Helianthus Annuus), Vanilla Aroma, Mentha Piperita (Peppermint) Leaf Oil, Dipteryx Odorata (Tonka Bean) Oil</p>
      <p class="info__maker">TERRABLOOM.CA<br>Made by Terra Bloom, Ridgeview, AB T0X 0X0</p>
    </div>
  </section>

  <!-- Marshmallow Creme -->
  <section class="label label--front marsh" style="left:651px;top:86px">
    <div class="art art--base" role="img" aria-label="Line drawing of mallow flowers and leaves"></div>
    <div class="tab">
      <div class="tab__kind">LIP BALM</div>
      <div class="title"><span class="title__name" style="--name-size:25px;left:8px">MARSHMALLOW<span class="title__flavour">creme</span></span></div>
    </div>
  </section>
  <section class="label label--wrap marsh" style="left:813px;top:120px">
    <div class="art art--corner" role="img" aria-label="Line drawing of a mallow flower with leaves"></div>
    <div class="art art--base" role="img" aria-label="Line drawing of mallow flowers and leaves"></div>
    <div class="tab">
      <div class="tab__kind">LIP BALM</div>
      <div class="title"><span class="title__name" style="--name-size:24px;left:8px">MARSHMALLOW<span class="title__flavour">creme</span></span></div>
    </div>
    <div class="info">
      <div class="info__claims"><span>plant based</span><span>vegan</span><span>cruelty free</span></div>
      <p class="info__ingredients"><strong>Ingredients:</strong>Organic Olive Fruit Oil (Olea Europaea), Organic Coconut Oil (Cocos Nucifera), Organic Shea Butter (Butyrospermum Parkii), Organic Jojoba Seed Oil (Simmondsia Chinensis), Rosehip Seed Oil (Rosa Canina), Vitamin E (Tocopherol), Sun Flower Oil (Helianthus Annuus), Vanilla Aroma, Dipteryx Odorata (Tonka Bean) Oil</p>
      <p class="info__maker">TERRABLOOM.CA<br>Made by Terra Bloom, Ridgeview, AB T0X 0X0</p>
    </div>
  </section>

  <!-- Coconut Lime -->
  <section class="label label--front coco" style="left:102px;top:570px">
    <div class="art art--base" role="img" aria-label="Line drawing of coconuts"></div>
    <div class="tab">
      <div class="tab__kind">LIP BALM</div>
      <div class="title"><span class="title__name" style="--name-size:42px;left:10px">COCONUT<span class="title__flavour">lime</span></span></div>
    </div>
  </section>
  <section class="label label--wrap coco" style="left:268px;top:602px">
    <div class="art art--corner" role="img" aria-label="Line drawing of lime slices and coconut"></div>
    <div class="art art--base" role="img" aria-label="Line drawing of coconuts"></div>
    <div class="tab">
      <div class="tab__kind">LIP BALM</div>
      <div class="title"><span class="title__name" style="--name-size:40px;left:10px">COCONUT<span class="title__flavour">lime</span></span></div>
    </div>
    <div class="info">
      <div class="info__claims"><span>plant based</span><span>vegan</span><span>cruelty free</span></div>
      <p class="info__ingredients"><strong>Ingredients:</strong>Organic Olive Fruit Oil (Olea Europaea), Organic Coconut Oil (Cocos Nucifera), Organic Shea Butter (Butyrospermum Parkii), Organic Jojoba Seed Oil (Simmondsia Chinensis), Rosehip Seed Oil (Rosa Canina), Vitamin E (Tocopherol), Sun Flower Oil (Helianthus Annuus), Vanilla Aroma, Dipteryx Odorata (Tonka Bean) Oil</p>
      <p class="info__maker">TERRABLOOM.CA<br>Made by Terra Bloom, Ridgeview, AB T0X 0X0</p>
    </div>
  </section>

  <!-- Citrus Spice -->
  <section class="label label--front citrus" style="left:651px;top:570px">
    <div class="art art--base" role="img" aria-label="Line drawing of orange slices and leaves"></div>
    <div class="tab">
      <div class="tab__kind">LIP BALM</div>
      <div class="title"><span class="title__name" style="--name-size:50px">CITRUS<span class="title__flavour">spice</span></span></div>
    </div>
  </section>
  <section class="label label--wrap citrus" style="left:813px;top:604px">
    <div class="art art--corner" role="img" aria-label="Line drawing of orange slices"></div>
    <div class="art art--base" role="img" aria-label="Line drawing of oranges and leaves"></div>
    <div class="tab">
      <div class="tab__kind">LIP BALM</div>
      <div class="title"><span class="title__name" style="--name-size:46px">CITRUS<span class="title__flavour">spice</span></span></div>
    </div>
    <div class="info">
      <div class="info__claims"><span>plant based</span><span>vegan</span><span>cruelty free</span></div>
      <p class="info__ingredients"><strong>Ingredients:</strong>Organic Olive Fruit Oil (Olea Europaea), Organic Coconut Oil (Cocos Nucifera), Organic Shea Butter (Butyrospermum Parkii), Organic Jojoba Seed Oil (Simmondsia Chinensis), Rosehip Seed Oil (Rosa Canina), Vitamin E (Tocopherol), Sun Flower Oil (Helianthus Annuus), Vanilla Aroma, Mentha Piperita (Peppermint) Leaf Oil, Dipteryx Odorata (Tonka Bean) Oil</p>
      <p class="info__maker">TERRABLOOM.CA<br>Made by Terra Bloom, Ridgeview, AB T0X 0X0</p>
    </div>
  </section>

</main>
</body>
</html>
```